Eco friendly Swedish beauty products sold in aluminum bottles - label design needed

We need help in designing a series of stick on labels for 80 ml (2.7 fl. oz.) aluminum bottles containing beauty products such as soaps, shampoo etc. The diameter of the bottle is 36 mm and the body of the bottles measures approx. 106 mm.
It is important for us that the label has a simplistic and clean feel with few colors (and the right ones!) and that the label helps amplify this product being both better and a more sustainable alternative to many of our plastic bottle competitors. The design and label should communicate the feel of an Eco-friendly, sustainable and modern brand of high quality - and with a Swedish concept.
We are using Montserrat font in our materials. Find attached information of preferred colors, the bottles and one example of our logotype. I am also available on e-mail should further information be needed.

Looking forward and very excited to receive your suggestions.
Note that we are expecting to start selling a series of approximately 10 different products where I will need one "master design" and then only smaller changes for each of the different products.

Target Market(s)

People whom are aware and not only look at price tag. Private and commercial market.

Industry/Entity Type

Beauty

Font styles to use
Other font styles liked:
• Montserrat

Requirements
Must have
• It must give the feel of being both better and a more sustainable alternative to many of our plastic bottle competitors.
Nice to have
• Simplistic. Clean. Clear.
Should not have
• Wrong colors, too complex designs.

```html
<!DOCTYPE html>
<html lang="en">
<head>
<meta charset="utf-8">
<title>Hand Sanitizer Label</title>
<link rel="stylesheet" href="https://fonts.googleapis.com/css2?family=Montserrat:wght@400;500;600&display=swap">
<style>
  :root {
    --label-green: #6e7a3a;
    --label-white: #ffffff;
    --brand-grey: #666666;
    --page-bg: #ffffff;
  }
  html, body {
    margin: 0;
    padding: 0;
    width: 1200px;
    height: 903px;
    overflow: hidden;
    background: var(--page-bg);
  }
  .label-art {
    display: block;
    width: 1200px;
    height: 903px;
    font-family: "Montserrat", sans-serif;
  }
  .brand-name { fill: var(--brand-grey); font-weight: 400; font-size: 155px; }
  .brand-tagline { fill: var(--brand-grey); font-weight: 400; font-size: 26px; }
  .label-field { fill: var(--label-green); }
  .label-stripe { fill: var(--label-white); }
  .label-text { fill: var(--label-white); }
  .product-line { font-weight: 400; font-size: 105px; }
  .product-type { font-weight: 500; font-size: 64px; }
  .percent-sign { font-weight: 600; font-size: 105px; }
  .claim-small { font-weight: 400; font-size: 30px; }
  .claim-large { font-weight: 400; font-size: 55px; }
  .zero-mark, .uses-frame { fill: none; stroke: var(--label-white); }
  .uses-small { font-weight: 400; font-size: 27px; }
  .uses-number { font-weight: 400; font-size: 44px; }
  .volume { font-weight: 400; font-size: 30px; }
  .fingerprint-icon { fill: var(--label-white); }
</style>
</head>
<body>
<svg class="label-art" viewBox="810 200 1595 1200" xmlns="http://www.w3.org/2000/svg" aria-label="Hand sanitizer label">
  <!-- brand column -->
  <text class="brand-name" transform="translate(1328 1382) rotate(-90)" textLength="1124" lengthAdjust="spacing">LINDHOLM</text>
  <text class="brand-tagline" transform="translate(1385 1370) rotate(-90)" textLength="1110" lengthAdjust="spacing">ECO FRIENDLY SWEDISH BEAUTY PRODUCTS</text>

  <!-- label panel -->
  <rect class="label-field" x="1422" y="262" width="573" height="1120"/>
  <rect class="label-stripe" x="1438" y="262" width="10" height="1120"/>
  <rect class="label-stripe" x="1464" y="262" width="10" height="1120"/>
  <rect class="label-stripe" x="1422" y="1247" width="573" height="10"/>
  <rect class="label-stripe" x="1422" y="1273" width="573" height="10"/>

  <!-- product name -->
  <text class="label-text product-line" x="1538" y="420" textLength="387" lengthAdjust="spacing">HAND</text>
  <circle class="fingerprint-icon" cx="1727" cy="533" r="58" role="img" aria-label="Fingerprint icon"/>
  <text class="label-text product-type" x="1530" y="687" textLength="392" lengthAdjust="spacing">SANITIZER</text>

  <!-- alcohol claim -->
  <rect class="zero-mark" x="-36" y="-92" width="72" height="184" rx="36" stroke-width="18" transform="translate(1533 887) rotate(20)"/>
  <text class="label-text percent-sign" x="1618" y="925">%</text>
  <text class="label-text claim-small" x="1722" y="870" textLength="190" lengthAdjust="spacing">ALCOHOL</text>
  <text class="label-text claim-large" x="1722" y="925" textLength="193" lengthAdjust="spacing">FREE</text>

  <!-- uses badge -->
  <rect class="uses-frame" x="1647" y="1034" width="139" height="140" stroke-width="3"/>
  <text class="label-text uses-small" x="1716" y="1075" text-anchor="middle" letter-spacing="3">UP TO</text>
  <text class="label-text uses-number" x="1716" y="1120" text-anchor="middle" letter-spacing="4">200</text>
  <text class="label-text uses-small" x="1716" y="1155" text-anchor="middle" letter-spacing="3">USES</text>

  <!-- volume -->
  <text class="label-text volume" x="1718" y="1340" text-anchor="middle">2.7 fl. Oz. (80 mg.)</text>
</svg>
</body>
</html>
```